Empresa de tecnología busca diseño de tarjetas de presentación

Se requiere tarjeta de presentación impresa, con los datos de contacto y logo de la empresa. (se adjunta una imagen como referencia, esto no significa que deberá de ser igual)

```html
<!DOCTYPE html>
<html lang="en">
<head>
<meta charset="utf-8">
<title>Velora IT – Business Cards</title>
<link rel="stylesheet" href="https://fonts.googleapis.com/css2?family=Mulish:wght@300;400;500;700;800&display=swap">
<style>
  :root {
    --navy: #1b3f72;
    --green: #6cb444;
    --ink: #2a2a2a;
    --rule: #8a8a8a;
    --card: #f6f6f6;
    --page: #ffffff;
  }
  * { margin: 0; padding: 0; box-sizing: border-box; }
  html, body { width: 900px; height: 1200px; overflow: hidden; background: var(--page); }
  body { position: relative; font-family: "Mulish", sans-serif; color: var(--ink); }

  .card {
    position: absolute;
    left: 78px;
    width: 758px;
    height: 436px;
    border-radius: 22px;
    background: var(--card);
    overflow: hidden;
  }
  .card--front { top: 134px; }
  .card--back { top: 639px; }

  .brand {
    position: absolute;
    display: flex;
    align-items: center;
    font-family: "Mulish", sans-serif;
    font-weight: 800;
    color: var(--navy);
    white-space: nowrap;
  }
  .brand__dot { border-radius: 50%; background: var(--green); flex: none; }
  .card--front .brand { left: 49px; top: 44px; font-size: 40px; letter-spacing: 3px; gap: 10px; }
  .card--front .brand__dot { width: 12px; height: 12px; }
  .card--back .brand { left: 0; right: 0; top: 165px; justify-content: center; font-size: 76px; letter-spacing: 8px; gap: 18px; }
  .card--back .brand__dot { width: 20px; height: 20px; }

  .person__name {
    position: absolute; left: 49px; top: 178px;
    font-size: 31px; font-weight: 400; color: var(--navy);
  }
  .person__role {
    position: absolute; left: 49px; top: 220px;
    font-size: 17px; font-weight: 500; color: var(--ink);
  }
  .person__rule {
    position: absolute; left: 49px; top: 249px;
    width: 42px; height: 1.5px; background: var(--rule);
  }

  .contact-list {
    position: absolute; left: 49px; top: 274px;
    list-style: none;
  }
  .contact-list li {
    display: flex; align-items: center; gap: 10px;
    height: 22px; font-size: 17px; font-weight: 300; color: var(--ink);
  }
  .contact-list svg { width: 14px; height: 14px; fill: var(--navy); flex: none; }

  .support-band {
    position: absolute; left: 0; right: 0; top: 372px; height: 34px;
    background: var(--green); color: #fff;
    display: flex; align-items: center; justify-content: center;
    font-size: 17px; font-weight: 300;
  }

  .web-address {
    position: absolute; left: 0; right: 0; top: 392px;
    text-align: center; font-size: 16px; font-weight: 500;
    letter-spacing: 4px; color: var(--navy);
  }
  .web-address .accent { color: var(--green); }
</style>
</head>
<body>

<section class="card card--front">
  <div class="brand"><span>Velora IT</span><span class="brand__dot"></span></div>

  <h1 class="person__name">Lucía Ortega</h1>
  <p class="person__role">Digital Marketing Manager</p>
  <div class="person__rule"></div>

  <ul class="contact-list">
    <li>
      <svg viewBox="0 0 24 24" aria-hidden="true"><path d="M6.6 10.8a15.2 15.2 0 0 0 6.6 6.6l2.2-2.2a1 1 0 0 1 1-.25 11.4 11.4 0 0 0 3.6.57 1 1 0 0 1 1 1V20a1 1 0 0 1-1 1A17 17 0 0 1 3 4a1 1 0 0 1 1-1h3.5a1 1 0 0 1 1 1c0 1.25.2 2.45.57 3.57a1 1 0 0 1-.25 1z"/></svg>
      (55) 4127 3890 ext. 1 24
    </li>
    <li>
      <svg viewBox="0 0 24 24" aria-hidden="true"><path d="M2 9c0-3 4.5-5 10-5s10 2 10 5v1.5h-5V8.5c-1.5-.6-3.2-.9-5-.9s-3.5.3-5 .9v2H2z"/><path d="M5 12h14l1 8H4z"/><circle cx="12" cy="15.8" r="2.2" fill="#f6f6f6"/></svg>
      56 2294 0718
    </li>
    <li>
      <svg viewBox="0 0 24 24" aria-hidden="true"><path d="M2 5h20v14H2z"/><path d="M2 5l10 8 10-8" fill="none" stroke="#f6f6f6" stroke-width="1.8"/></svg>
      lu.ortega@velorait.com
    </li>
    <li>
      <svg viewBox="0 0 24 24" aria-hidden="true"><path d="M12 2a7 7 0 0 0-7 7c0 5.2 7 13 7 13s7-7.8 7-13a7 7 0 0 0-7-7zm0 9.5A2.5 2.5 0 1 1 12 6.5a2.5 2.5 0 0 1 0 5z"/></svg>
      12th floor, Marven Tower CDMX
    </li>
  </ul>

  <div class="support-band">Do you need to lift a ticket? 01 800 3100482</div>
</section>

<section class="card card--back">
  <div class="brand"><span>Velora IT</span><span class="brand__dot"></span></div>
  <p class="web-address">www.<span class="accent">support@velorait</span>.com</p>
</section>

</body>
</html>
```